Psychotherapist need a business card with logo

I am a psychotherapist in need of a business card. The card must have:

Marisol Trevuneda
Psicoterapeuta
937 281 706

Psychologists use the greek letter psy, which is the psychologist symbol, but I would prefer something like a mandala, a graphic symbol, an iconic tree, nothing very usual, but something that shows confidence and trust.

Industry/Entity Type

Business

```html
<!DOCTYPE html>
<html lang="es">
<head>
<meta charset="utf-8">
<title>Marisol Trevuneda — Psicoterapeuta</title>
<link href="https://fonts.googleapis.com/css2?family=PT+Sans:wght@400&display=swap" rel="stylesheet">
<style>
  :root {
    --card-green: #2f5529;
    --shade-green: #294a24;
    --tree-white: #ffffff;
    --tree-pale: #e6ece4;
    --ink-light: #ffffff;
  }
  html, body {
    margin: 0;
    padding: 0;
    width: 1200px;
    height: 702px;
    overflow: hidden;
    background: var(--card-green);
  }
  .business-card {
    position: relative;
    width: 1200px;
    height: 702px;
    background: var(--card-green);
    overflow: hidden;
    font-family: "PT Sans", "Myriad Pro", Arial, sans-serif;
  }
  .backdrop-tree {
    position: absolute;
    left: 221px;
    top: 0;
    width: 730px;
    height: 702px;
    background: radial-gradient(closest-side, var(--shade-green) 0%, rgba(41, 74, 36, 0.55) 55%, rgba(47, 85, 41, 0) 100%);
  }
  .emblem-tree {
    position: absolute;
    left: 88px;
    top: 124px;
    width: 498px;
    height: 473px;
    background: radial-gradient(closest-side, var(--tree-white) 0%, var(--tree-pale) 60%, rgba(230, 236, 228, 0) 100%);
  }
  .contact-block {
    position: absolute;
    right: 83px;
    top: 222px;
    text-align: right;
    color: var(--ink-light);
    font-weight: 400;
    font-size: 66px;
    line-height: 82px;
    white-space: nowrap;
  }
  .contact-block p {
    margin: 0;
  }
</style>
</head>
<body>
  <main class="business-card">
    <div class="backdrop-tree" role="img" aria-label="Large faint silhouette of a bare tree in darker green behind the card"></div>
    <div class="emblem-tree" role="img" aria-label="White emblem of a bare tree with spreading branches"></div>
    <section class="contact-block">
      <p class="person-name">Marisol Trevuneda</p>
      <p class="person-role">Psicoterapeuta</p>
      <p class="person-phone">937 281 706</p>
    </section>
  </main>
</body>
</html>
```